Need a business card for our overland brand!

We had the logo made and we need a great design for our business card. Use the logo provide or tweak it however you see fit.

Contact Information for Business Card

Name, Title, Telephone, email, website

```html
<!DOCTYPE html>
<html lang="en">
<head>
<meta charset="utf-8">
<title>Ridgeline Roaming – Business Card</title>
<link href="https://fonts.googleapis.com/css2?family=Montserrat:wght@400;700;800&display=swap" rel="stylesheet">
<style>
  :root {
    --backdrop: #acacac;
    --card: #ffffff;
    --navy: #263a52;
    --teal: #1fa0c3;
    --ink: #2b3a4d;
  }
  * { margin: 0; padding: 0; box-sizing: border-box; }
  html, body { width: 1200px; height: 1000px; overflow: hidden; }
  body {
    background: var(--backdrop);
    font-family: "Montserrat", Arial, sans-serif;
    position: relative;
  }
  .card {
    position: absolute;
    left: 294px;
    width: 613px;
    height: 351px;
    background: var(--card);
    border-radius: 28px;
    overflow: hidden;
  }
  .card--front { top: 96px; }
  .card--back { top: 518px; }

  .brand-name {
    position: absolute;
    color: var(--navy);
    font-weight: 800;
    text-transform: uppercase;
    text-align: center;
    line-height: 1.05;
    letter-spacing: 0.5px;
  }
  .card--front .brand-name {
    left: 0; right: 0;
    top: 128px;
    font-size: 50px;
  }
  .card--back .brand-name {
    left: 80px;
    width: 156px;
    top: 210px;
    font-size: 27px;
  }

  .mountain-band {
    position: absolute;
    left: 0; top: 0;
    width: 613px;
    height: 170px;
    background: linear-gradient(180deg, var(--navy) 0%, var(--navy) 55%, var(--teal) 100%);
  }

  .contact {
    position: absolute;
    left: 313px;
    width: 200px;
    top: 183px;
    text-align: center;
    color: var(--ink);
  }
  .contact__name { font-size: 15px; font-weight: 700; line-height: 20px; }
  .contact__title { font-size: 15px; font-weight: 400; line-height: 20px; }
  .contact__icons {
    display: flex;
    justify-content: center;
    gap: 4px;
    margin: 8px 0 6px;
  }
  .contact__icons svg { width: 24px; height: 24px; display: block; }
  .contact__line { font-size: 13.5px; line-height: 17px; }
</style>
</head>
<body>

  <section class="card card--front">
    <div class="brand-name">Ridgeline<br>Roaming</div>
  </section>

  <section class="card card--back">
    <div class="mountain-band" role="img" aria-label="Jagged mountain range silhouette in navy and teal"></div>

    <div class="brand-name">Ridgeline<br>Roaming</div>

    <div class="contact">
      <div class="contact__name">Name Surname</div>
      <div class="contact__title">Title</div>
      <div class="contact__icons">
        <svg viewBox="0 0 24 24" aria-label="Phone">
          <circle cx="12" cy="12" r="12" fill="var(--teal)"/>
          <path d="M8.6 6.8l1.6-.4 1.2 2.6-1 .9c.5 1.2 1.4 2.1 2.6 2.7l.9-1 2.6 1.2-.4 1.6c-.2.5-.7.8-1.2.7-3.6-.5-6.5-3.4-7-7-.1-.5.2-1 .7-1.3z" fill="#fff"/>
        </svg>
        <svg viewBox="0 0 24 24" aria-label="Email">
          <circle cx="12" cy="12" r="12" fill="var(--teal)"/>
          <rect x="6.5" y="8" width="11" height="8" rx="1" fill="#fff"/>
          <path d="M6.8 8.4l5.2 4 5.2-4" fill="none" stroke="var(--teal)" stroke-width="1.1"/>
        </svg>
        <svg viewBox="0 0 24 24" aria-label="Website">
          <circle cx="12" cy="12" r="12" fill="var(--teal)"/>
          <g fill="none" stroke="#fff" stroke-width="1.1">
            <circle cx="12" cy="12" r="5.5"/>
            <ellipse cx="12" cy="12" rx="2.3" ry="5.5"/>
            <path d="M6.5 12h11M7.3 9.2h9.4M7.3 14.8h9.4"/>
          </g>
        </svg>
      </div>
      <div class="contact__line">1234-567-890</div>
      <div class="contact__line">email@website.com</div>
      <div class="contact__line">website.com</div>
    </div>
  </section>

</body>
</html>
```